A website design for a consultation firm

We are located in Istanbul, Turkey and offers our consultation services to customers interested in investing in Realestate, Education and Investment particularly this coming from Arab world and English speaking countries.

The site should carry our message of deep knowledge about the Turkish markets in the mentioned sectors of interest, sincerity and keenness.

The final deliverable of the winning design should include:
- The source files of the final designs. e.g. AI, PSD ..etc
- The redline markup for the design using a Specctr or any other similar tool.

Target Market(s)

English and Arabic speaking countries with a Turkish theme since we are a Turkish company

Industry/Entity Type

Consulting

Number of Pages Required

2 page

Font styles to use
Sans Serif

Requirements
Must have
• The site should serve the following main sections:
• - Why QVD?
• - Reports & studies
• - Sectors
• - Our team
• - Contact
• We need a design that could be converted into a WordPress theme.
• The design should be in English but should accommodate other languages including RTL.
• You can use the color theme you like as long as it does't dissolve the logo.
• The site should link into our accounts on the following networks:
• - Twitter
• - Facebook
• - LinkedIn
• The design should be responsive and nicely rendered on Desktop, Tablets and Smart phones.
Nice to have
• The site would be nice to balance between being informative and

```html
<!DOCTYPE html>
<html lang="en">
<head>
<meta charset="utf-8">
<title>QVD Consulting</title>
<link rel="stylesheet" href="https://fonts.googleapis.com/css2?family=Dosis:wght@500;600;700&family=Open+Sans:wght@400;600;700&display=swap">
<style>
:root{
  --red:#d0102b;
  --red-dark:#a50b20;
  --navy:#1c3461;
  --navy-dark:#152848;
  --ink:#222;
  --text:#555;
  --light:#f1f1f1;
  --night:#0c131d;
  --white:#fff;
}
*{box-sizing:border-box;margin:0;padding:0}
html,body{width:1200px;height:3082px;overflow:hidden}
body{font-family:"Open Sans",Arial,sans-serif;color:var(--text);background:var(--white);position:relative}
section,header,footer,nav{position:absolute;left:0;width:1200px}
.abs{position:absolute}
.heading{font-family:"Dosis",Arial,sans-serif;font-weight:700;font-size:30px;color:var(--ink);text-align:center;letter-spacing:.5px;width:100%}
.heading em{font-style:normal;color:var(--red)}
.divider{position:absolute;left:450px;width:300px;height:1px;background:#ccc}
.divider::after{content:"";position:absolute;left:145px;top:-5px;width:10px;height:10px;border-radius:50%;background:var(--white);border:1px solid #bbb}
.intro{position:absolute;left:230px;width:740px;text-align:center;font-size:13px;line-height:20px;color:#444}
.btn{position:absolute;display:flex;align-items:center;justify-content:center;font-size:12px;font-weight:600;color:var(--white);border-radius:2px}
.btn-red{background:var(--red)}
.btn-navy{background:var(--navy)}
.btn-black{background:#111}

/* top bar */
.topbar{top:0;height:40px;background:var(--red);z-index:1}
.social-dot{width:12px;height:12px;border-radius:50%;background:var(--white);top:14px}
.topbar .phone{left:296px;top:11px;color:var(--white);font-size:14px;display:flex;gap:8px;align-items:center}
.lang{top:12px;color:var(--white);font-size:12px}
.appointment{left:935px;top:0;width:102px;height:40px;background:var(--red-dark);color:var(--white);font-size:12px;font-weight:600;display:flex;align-items:center;justify-content:center}
.nav-sep{top:0;width:1px;height:40px;background:rgba(255,255,255,.3)}

/* nav */
.nav{top:40px;height:82px;background:var(--white);box-shadow:0 2px 4px rgba(0,0,0,.08);z-index:2}
.nav a{position:absolute;top:30px;font-size:13px;color:#333;text-decoration:none;letter-spacing:.3px;white-space:nowrap}
.nav a.active{color:var(--red)}
.logo-box{left:544px;top:-24px;width:124px;height:100px;background:var(--white);box-shadow:0 1px 6px rgba(0,0,0,.18);display:flex;flex-direction:column;align-items:center;justify-content:center;gap:2px}
.logo-name{font-family:"Open Sans",Arial,sans-serif;font-weight:700;color:var(--red);font-size:34px;line-height:1}
.logo-sub{font-family:"Open Sans",Arial,sans-serif;font-weight:700;color:var(--red);font-size:15px;line-height:1}

/* hero */
.hero{top:122px;height:449px}
.hero-photo{position:absolute;inset:0;background:linear-gradient(100deg,#e9eef3 0%,#cfd6dc 30%,#b9c0c6 55%,#d8dde2 80%,#eef0f2 100%)}
.hero-kicker{left:160px;top:160px;font-family:"Dosis",Arial,sans-serif;font-weight:600;font-size:19px;color:#222}
.hero-title{left:160px;top:180px;font-family:"Dosis",Arial,sans-serif;font-weight:700;font-size:36px;color:#111;letter-spacing:.5px}
.hero-text{left:162px;top:228px;width:320px;font-size:12px;line-height:18px;color:#222}

/* about */
.about{top:571px;height:477px;background:var(--white)}
.about-photo{position:absolute;left:600px;top:0;width:600px;height:477px;background:linear-gradient(90deg,#fff 0%,#e7e9eb 25%,#d4d6d8 60%,#eceef0 100%)}
.about-logo{left:286px;top:50px;display:flex;flex-direction:column;align-items:center;gap:2px}
.about-logo .logo-name{font-size:58px}
.about-logo .logo-sub{font-size:20px}
.about-title{left:160px;top:178px;width:400px;text-align:center;font-family:"Dosis",Arial,sans-serif;font-weight:700;font-size:28px;color:var(--ink)}
.about-title em{font-style:normal;color:var(--red)}
.about-text{left:150px;top:218px;width:420px;text-align:center;font-size:12px;line-height:21px;color:#333}

/* sectors */
.sectors{top:1048px;height:541px;background:var(--light)}
.card{position:absolute;top:170px;width:278px;height:300px;background:var(--white)}
.card-img{height:155px}
.card h3{margin-top:17px;text-align:center;font-family:"Dosis",Arial,sans-serif;font-weight:700;font-size:16px;color:var(--red)}
.card p{width:220px;margin:10px auto 0;text-align:center;font-size:12px;line-height:19px;color:#444}
.card .btn{left:81px;top:282px;width:116px;height:34px}
.slide-arrow{top:300px}

/* why */
.why{top:1589px;height:517px;background:var(--white)}
.why-photo{left:460px;top:150px;width:300px;height:367px;background:radial-gradient(ellipse at 50% 55%,#5c5f66 0%,#8a8d93 35%,#e8e9eb 70%,#fff 100%)}
.feat-icon{width:52px;height:52px;border-radius:50%;background:var(--navy);border:3px solid var(--white);box-shadow:0 0 0 1px var(--navy);display:flex;align-items:center;justify-content:center}
.feat{width:230px;font-size:11px;line-height:17px;color:#333}
.feat h4{font-size:13px;font-weight:700}
.feat.left{text-align:right}
.feat.left h4{color:var(--navy)}
.feat.right h4{color:var(--red)}

/* team */
.team{top:2106px;height:452px;background:var(--light)}
.member{position:absolute;top:160px;width:198px;height:256px}
.member-photo{position:absolute;inset:0}
.member-name{position:absolute;left:0;bottom:0;width:100%;height:52px;background:rgba(28,52,97,.92);color:var(--white);text-align:center;padding-top:9px}
.member-name b{display:block;font-size:13px}
.member-name span{font-size:11px}
.member.featured{background:var(--navy);color:var(--white);text-align:center;border-left:8px solid var(--red)}
.member.featured b{display:block;margin-top:26px;font-size:13px}
.member.featured .role{font-size:11px}
.member.featured p{width:150px;margin:22px auto 0;font-size:11px;line-height:17px}
.member-social{display:flex;gap:8px;justify-content:center;margin-top:16px}
.member-social i{width:20px;height:20px;border-radius:50%;background:var(--white);display:block}

/* help band */
.help{top:2558px;height:93px;background:var(--white)}
.help-navy{position:absolute;left:0;top:10px;width:1200px;height:83px;background:var(--navy)}
.help-red{position:absolute;left:0;top:0;width:510px;height:93px}
.help-title{left:205px;top:18px;font-family:"Dosis",Arial,sans-serif;font-weight:600;font-size:26px;line-height:27px;color:var(--white)}
.help-call{left:540px;top:40px;color:var(--white);font-size:16px}
.help-num{left:684px;top:28px;color:var(--white);font-size:29px;font-weight:700;letter-spacing:.5px}

/* contact */
.contact{top:2651px;height:386px;background:var(--night)}
.contact .heading{color:var(--white)}
.contact-map{left:640px;top:90px;width:380px;height:230px;background:radial-gradient(ellipse at center,rgba(255,255,255,.06) 0%,rgba(255,255,255,0) 70%)}
.contact h5{position:absolute;font-size:16px;font-weight:700;color:var(--white)}
.field{position:absolute;left:160px;width:363px;border:1px solid #2c3441;background:#0f1722;color:#ddd;font-size:11px;padding:5px 8px}
.detail{position:absolute;left:652px;display:flex;gap:14px;font-size:12px;line-height:19px;color:#ddd}
.follow{left:652px;top:330px;display:flex;gap:14px}
.follow i{display:block;width:24px;height:24px}

footer{top:3037px;height:45px;background:var(--white);text-align:center;font-size:11px;color:#333;padding-top:14px}
</style>
</head>
<body>

<header class="topbar">
  <i class="abs social-dot" style="left:172px"></i>
  <i class="abs social-dot" style="left:196px"></i>
  <i class="abs social-dot" style="left:220px"></i>
  <i class="abs social-dot" style="left:244px"></i>
  <div class="nav-sep abs" style="left:275px"></div>
  <div class="abs phone">
    <svg width="15" height="15" viewBox="0 0 24 24"><path fill="#fff" d="M6.6 10.8a15.1 15.1 0 0 0 6.6 6.6l2.2-2.2c.3-.3.7-.4 1-.2 1.1.4 2.3.6 3.6.6.6 0 1 .4 1 1V20c0 .6-.4 1-1 1A17 17 0 0 1 3 4c0-.6.4-1 1-1h3.5c.6 0 1 .4 1 1 0 1.3.2 2.5.6 3.6.1.3 0 .7-.2 1z"/></svg>
    0100 555 020
  </div>
  <span class="abs lang" style="left:760px">English</span>
  <span class="abs lang" style="left:829px">Arabic</span>
  <span class="abs lang" style="left:892px">Urdu</span>
  <div class="abs appointment">Appointment</div>
</header>

<nav class="nav">
  <a class="active" style="left:168px">HOME</a>
  <span class="abs" style="left:168px;top:52px;width:40px;height:2px;background:var(--red)"></span>
  <a style="left:262px">WHY US ?</a>
  <a style="left:370px">REPORTS &amp; STUDIES</a>
  <div class="abs logo-box"><span class="logo-name">QVD</span><span class="logo-sub">consulting</span></div>
  <a style="left:712px">SECTORS</a>
  <a style="left:824px">OUR TEAM</a>
  <a style="left:946px">CONTACT US</a>
</nav>

<section class="hero">
  <div class="hero-photo" role="img" aria-label="Advisers meeting with clients around an office table"></div>
  <div class="abs hero-kicker">GREAT EXPERIENCE</div>
  <div class="abs hero-title">MEET OUR ADVISER</div>
  <p class="abs hero-text">Comprehensive financial advice and financial services that are tailored to meet your individual needs.</p>
  <div class="btn btn-red" style="left:160px;top:280px;width:118px;height:34px">Learn More</div>
  <div class="btn btn-black" style="left:290px;top:280px;width:136px;height:34px">Quick Call Back</div>
</section>

<section class="about">
  <div class="about-photo" role="img" aria-label="Three business professionals standing with arms crossed"></div>
  <div class="abs about-logo"><span class="logo-name">QVD</span><span class="logo-sub">consulting</span></div>
  <h2 class="abs about-title">ABOUT <em>QVD CONSULTING</em></h2>
  <p class="abs about-text">c Ut wisi enim ad minim veniam, quis nostrud exerci tation ullamcorper suscipit lobortis nisl ut aliquip ex ea commodo consequat. Duis autem vel eum iriure dolor in hendrerit in vulputate velit esse molestie consequat, vel illum dolore eu feugiat nulla facilisis at vero eros et accumsan et iusto odio dignissim qui blandit praesent luptatum zzril delenit augue duis dolore te feugait nulla facilisi.</p>
  <div class="btn btn-navy" style="left:302px;top:405px;width:118px;height:34px">Contact Us</div>
</section>

<section class="sectors">
  <h2 class="heading abs" style="top:50px">OUR <em>SECTORS</em></h2>
  <div class="divider" style="top:100px"></div>
  <p class="intro" style="top:112px">Lorem ipsum dolor sit amet, consectetuer adipiscing elit, sed diam nonummy nibh euismod tincidunt ut laoreet dolore magna aliquam erat volutpat.</p>
  <svg class="abs slide-arrow" style="left:110px" width="24" height="50" viewBox="0 0 24 50"><path d="M20 2 4 25l16 23" fill="none" stroke="#bbb" stroke-width="2"/></svg>
  <svg class="abs slide-arrow" style="left:1066px" width="24" height="50" viewBox="0 0 24 50"><path d="M4 2l16 23L4 48" fill="none" stroke="#bbb" stroke-width="2"/></svg>
  <article class="card" style="left:162px">
    <div class="card-img" role="img" aria-label="Businessman touching a rising chart" style="background:linear-gradient(135deg,#0f1e33,#3b5a7a)"></div>
    <h3>REAL ESTATE INVESTMENT</h3>
    <p>Lorem ipsum dolor sit amet, eiusmod tempor incididunt ut labore et dolore magna aliqua.</p>
    <div class="btn btn-navy">Read More</div>
  </article>
  <article class="card" style="left:460px">
    <div class="card-img" role="img" aria-label="Hands reviewing financial charts on a tablet" style="background:linear-gradient(135deg,#e9ecef,#aab4bd)"></div>
    <h3>INVESTMENT MANAGEMENT</h3>
    <p>Lorem ipsum dolor sit amet, eiusmod tempor incididunt ut labore et dolore magna aliqua.</p>
    <div class="btn btn-navy">Read More</div>
  </article>
  <article class="card" style="left:760px">
    <div class="card-img" role="img" aria-label="Graduates in caps against a bright sky" style="background:linear-gradient(180deg,#cfe0ef,#2a2c31)"></div>
    <h3>EDUCATION</h3>
    <p>Lorem ipsum dolor sit amet, eiusmod tempor incididunt ut labore et dolore magna aliqua.</p>
    <div class="btn btn-navy">Read More</div>
  </article>
</section>

<section class="why">
  <h2 class="heading abs" style="top:40px">WHY <em>US ?</em></h2>
  <div class="divider" style="top:90px"></div>
  <p class="intro" style="top:102px">Lorem ipsum dolor sit amet, consectetuer adipiscing elit, sed diam nonummy nibh euismod tincidunt ut laoreet dolore magna aliquam erat volutpat.</p>
  <div class="abs why-photo" role="img" aria-label="Senior adviser in a suit holding a tablet"></div>

  <div class="abs feat-icon" style="left:364px;top:152px"><svg width="24" height="20" viewBox="0 0 24 20"><rect x="1" y="5" width="22" height="14" rx="2" fill="#fff"/><rect x="8" y="1" width="8" height="5" fill="none" stroke="#fff" stroke-width="2"/></svg></div>
  <div class="abs feat left" style="left:190px;top:210px"><h4>Experienced</h4>Lorem ipsum dolor sit amet,<br>eiusmod tempor incididunt ut labore .</div>

  <div class="abs feat-icon" style="left:364px;top:322px"><svg width="22" height="22" viewBox="0 0 22 22"><circle cx="11" cy="6" r="5" fill="#fff"/><path d="M1 22c0-6 4-9 10-9s10 3 10 9z" fill="#fff"/></svg></div>
  <div class="abs feat left" style="left:190px;top:380px"><h4>Professional</h4>Lorem ipsum dolor sit amet,<br>eiusmod tempor incididunt ut labore .</div>

  <div class="abs feat-icon" style="left:794px;top:152px"><svg width="22" height="22" viewBox="0 0 22 22"><circle cx="9" cy="9" r="7" fill="none" stroke="#fff" stroke-width="2"/><rect x="12" y="12" width="9" height="9" fill="#fff"/></svg></div>
  <div class="abs feat right" style="left:798px;top:210px"><h4>Specialists In (PFPS)</h4>Lorem ipsum dolor sit amet,<br>eiusmod tempor incididunt ut labore .</div>

  <div class="abs feat-icon" style="left:794px;top:322px"><svg width="24" height="22" viewBox="0 0 24 22"><path d="M2 20 12 2l10 18z" fill="none" stroke="#fff" stroke-width="2"/><rect x="10" y="10" width="4" height="6" fill="#fff"/></svg></div>
  <div class="abs feat right" style="left:798px;top:380px"><h4>Solid Securities</h4>Lorem ipsum dolor sit amet,<br>eiusmod tempor incididunt ut labore .</div>
</section>

<section class="team">
  <h2 class="heading abs" style="top:40px">MEET <em>THE TEAM</em></h2>
  <div class="divider" style="top:90px"></div>
  <p class="intro" style="top:102px">Lorem ipsum dolor sit amet, consectetuer adipiscing elit, sed diam nonummy nibh euismod tincidunt ut laoreet dolore magna aliquam erat volutpat.</p>
  <div class="member" style="left:162px">
    <div class="member-photo" role="img" aria-label="Portrait of a young adviser with glasses" style="background:linear-gradient(160deg,#d8d4cc,#8b8478)"></div>
    <div class="member-name"><b>DANIEL KORSEN</b><span>Financial Advisor</span></div>
  </div>
  <div class="member featured" style="left:388px">
    <b>LEYLA ARSLAN</b><span class="role">Financial Advisor</span>
    <p>c Ut wisi enim ad minim veniam, quis nostrud exerci tation ullamcorper suscipit lobortis nisl ut aliquip ex ea commodo consequat.</p>
    <div class="member-social"><i></i><i></i><i></i><i></i></div>
  </div>
  <div class="member" style="left:612px">
    <div class="member-photo" role="img" aria-label="Portrait of a female adviser with glasses" style="background:linear-gradient(160deg,#e2ddd6,#9b938a)"></div>
    <div class="member-name"><b>MIRA TOLVEN</b><span>Financial Advisor</span></div>
  </div>
  <div class="member" style="left:838px">
    <div class="member-photo" role="img" aria-label="Portrait of a young male adviser" style="background:linear-gradient(160deg,#cfd2d5,#7d8287)"></div>
    <div class="member-name"><b>KEREM AYDIN</b><span>Financial Advisor</span></div>
  </div>
</section>

<section class="help">
  <div class="help-navy"></div>
  <svg class="help-red" viewBox="0 0 510 93" preserveAspectRatio="none"><path d="M0 0h420l90 93H0z" fill="var(--red)"/></svg>
  <svg class="abs" style="left:160px;top:30px" width="28" height="28" viewBox="0 0 24 24"><path fill="#fff" d="M6.6 10.8a15.1 15.1 0 0 0 6.6 6.6l2.2-2.2c.3-.3.7-.4 1-.2 1.1.4 2.3.6 3.6.6.6 0 1 .4 1 1V20c0 .6-.4 1-1 1A17 17 0 0 1 3 4c0-.6.4-1 1-1h3.5c.6 0 1 .4 1 1 0 1.3.2 2.5.6 3.6.1.3 0 .7-.2 1z"/></svg>
  <div class="abs help-title">FOR ANY HELP<br>OR QUERIES</div>
  <div class="abs help-call">Call Us Now On</div>
  <div class="abs help-num">0100 555 020</div>
  <div class="btn btn-red" style="left:903px;top:36px;width:134px;height:34px">GET A QUOTE</div>
</section>

<section class="contact">
  <h2 class="heading abs" style="top:42px;color:var(--white)">GET <em>IN TOUCH</em></h2>
  <div class="divider" style="top:92px;background:#444"></div>
  <div class="abs contact-map" role="img" aria-label="Faint world map"></div>
  <h5 style="left:160px;top:102px">Drop us a line</h5>
  <div class="field" style="top:140px;height:29px">Name</div>
  <div class="field" style="top:179px;height:29px">Email</div>
  <div class="field" style="top:219px;height:29px">Phone</div>
  <div class="field" style="top:254px;height:60px">Message</div>
  <div class="btn btn-red" style="left:160px;top:321px;width:105px;height:34px;font-size:13px">SUBMIT</div>

  <h5 style="left:652px;top:102px">Contact Details</h5>
  <div class="detail" style="top:142px">
    <svg width="12" height="16" viewBox="0 0 12 16"><path d="M6 0a6 6 0 0 1 6 6c0 4-6 10-6 10S0 10 0 6a6 6 0 0 1 6-6z" fill="var(--red)"/><circle cx="6" cy="6" r="2" fill="var(--night)"/></svg>
    <span>Lorem ipsum dolor sit amet,<br>consectetuer adipiscing elit dolor.</span>
  </div>
  <div class="detail" style="top:200px">
    <svg width="12" height="14" viewBox="0 0 24 24"><path fill="var(--red)" d="M6.6 10.8a15.1 15.1 0 0 0 6.6 6.6l2.2-2.2c.3-.3.7-.4 1-.2 1.1.4 2.3.6 3.6.6.6 0 1 .4 1 1V20c0 .6-.4 1-1 1A17 17 0 0 1 3 4c0-.6.4-1 1-1h3.5c.6 0 1 .4 1 1 0 1.3.2 2.5.6 3.6.1.3 0 .7-.2 1z"/></svg>
    <span>+0100555020 &nbsp;&nbsp;or&nbsp;&nbsp; +0100555021</span>
  </div>
  <div class="detail" style="top:236px">
    <svg width="13" height="10" viewBox="0 0 13 10"><rect width="13" height="10" fill="var(--red)"/><path d="M0 0l6.5 5L13 0" fill="none" stroke="var(--night)"/></svg>
    <span>info@qvdconsulting.com</span>
  </div>
  <h5 style="left:652px;top:290px">Follow us</h5>
  <div class="abs follow">
    <i style="background:#3b5998"></i><i style="background:#1da1f2"></i><i style="background:#c0392b"></i><i style="background:#0e76a8"></i>
  </div>
</section>

<footer>Copyright © 2016 qvdconsulting. All Rights Reserved</footer>

</body>
</html>
```